Social Media Marketing website

Need website designed for social media marketing company BrightLoop.com
Do no currently have logo.
Pages:
Main
Services
Order
Contact
Please use dummy text for now. I will provide content to winner later to add.
Main page should clearly show the steps with some sort of graphic: Establish, Engage, Analyze.
Services provided (steps):
1) Establish social media presence
2) Social media management and advertising
3) Analyze and engage
Site should be simple, clean and attractive. Design examples:
http://plinkster.com/
http://www.quillbase.com/
http://www.harrowvalemq.com/
Be creative! It should not look like a template.
Updates
Updated examples.
Contact me for questions.
dave@brightloop.com
3) Analyze and engage
Advertising

```html
<!DOCTYPE html>
<html lang="en">
<head>
<meta charset="utf-8">
<title>BrightLoop – Social Media Marketing Company</title>
<link rel="stylesheet" href="https://fonts.googleapis.com/css2?family=Arimo:wght@400;700&display=swap">
<style>
:root{
  --wine:#8a3b4a;
  --wine-deep:#6e2a38;
  --wine-light:#b5606f;
  --teal-dark:#0f2a30;
  --page:#ececec;
  --panel:#f5f5f5;
  --ink:#333;
  --muted:#555;
  --link:#2a9cc4;
  --white:#fff;
  --footer:#0c1b1f;
  --accent:#d9304e;
}
*{box-sizing:border-box;margin:0;padding:0}
html,body{width:1199px;height:1200px;overflow:hidden}
body{font-family:"Arimo",Arial,sans-serif;background:var(--page);color:var(--ink);position:relative}
.backdrop-top{position:absolute;left:0;top:0;width:1199px;height:380px;
  background:radial-gradient(ellipse at 42% 0%,var(--wine-light) 0%,var(--wine) 45%,var(--wine-deep) 100%)}
.backdrop-band{position:absolute;left:0;top:380px;width:1199px;height:63px;background:var(--teal-dark)}
.backdrop-fade{position:absolute;left:0;top:443px;width:1199px;height:120px;background:linear-gradient(#fff,var(--page))}
.utility-bar{position:absolute;left:0;top:0;width:1199px;height:45px;background:rgba(0,0,0,.12);border-bottom:1px solid rgba(255,255,255,.15)}
.follow{position:absolute;left:195px;top:17px;font-size:10px;color:var(--white);display:flex;gap:4px;align-items:center}
.follow .net{width:12px;height:12px;background:#d8d8d8;display:inline-block;margin-left:2px}
.support{position:absolute;left:610px;top:17px;font-size:10px;color:var(--white)}
.search{position:absolute;left:852px;top:12px;width:156px;height:22px;background:var(--white);border:1px solid #555;font-size:10px;padding:4px 6px;color:#444}
.search .go{position:absolute;right:0;top:0;width:22px;height:20px;background:#2c4a55}
.logo{position:absolute;left:190px;top:70px;color:var(--white)}
.logo .name{font-size:33px;font-weight:700;letter-spacing:-.5px}
.logo .tag{font-size:10px;margin-top:1px}
.nav{position:absolute;left:641px;top:83px;display:flex;align-items:center;font-size:10px;color:var(--white)}
.nav a{color:var(--white);text-decoration:none;width:80px;text-align:center;height:26px;line-height:26px}
.nav a.current{width:67px;background:linear-gradient(#e9506a,var(--accent));border-radius:3px;margin-right:5px}
.rule{position:absolute;left:190px;top:142px;width:820px;height:1px;background:rgba(255,255,255,.3)}
.hero{position:absolute;left:190px;top:151px;width:820px;height:378px;border:5px solid #e8e8e8;
  background:linear-gradient(180deg,#3e3f6e 0%,#5a5f8c 35%,#3b3f4a 65%,#6b5a2e 85%,#2d3a2a 100%);box-shadow:0 2px 6px rgba(0,0,0,.3)}
.panel{position:absolute;left:190px;width:820px}
.welcome{top:544px;height:136px;background:var(--panel);border:1px solid #ddd}
.why{top:680px;height:140px}
.panel h2{position:absolute;left:17px;font-size:19px;font-weight:400;color:#444}
.welcome h2{top:18px}.why h2{top:16px}
.panel .icon{position:absolute;left:20px;width:48px;height:52px;border-radius:6px}
.welcome .icon{top:57px;background:linear-gradient(#d98a3c,#a55a1f)}
.why .icon{top:62px;background:linear-gradient(#b0703a,#7a4520)}
.panel p{position:absolute;left:89px;width:715px;font-size:10.5px;line-height:16px;color:var(--muted)}
.welcome p{top:60px}.why p{top:56px}
.divider{position:absolute;left:190px;top:818px;width:820px;height:6px;background:radial-gradient(ellipse at center,rgba(0,0,0,.12),transparent 70%)}
.step{position:absolute;top:860px;width:250px}
.step h3{font-size:14px;font-weight:700;color:#444}
.step .sub{display:block;font-size:9px;color:var(--link);margin-top:5px}
.step .banner{margin-top:16px;width:246px;height:67px;border:3px solid #ddd;display:flex;align-items:center;justify-content:center;font-size:19px;color:var(--white)}
.step .banner b{font-weight:700;margin:0 5px}
.step p{margin-top:16px;font-size:10px;line-height:16px;color:var(--muted)}
.step .more{display:block;font-size:10px;color:#222;margin-top:2px}
.s1{left:207px}.s1 .banner{background:linear-gradient(90deg,#f3e4ee,#f6b8d6,#f2d4e4);color:#888}
.s2{left:476px}.s2 .banner{background:linear-gradient(90deg,#8cc21c,#b9de3a,#7cb51b)}
.s3{left:745px}.s3 .banner{background:linear-gradient(90deg,#1b4fa8,#2f6ed0,#1a49a0)}
.footer{position:absolute;left:0;top:1150px;width:1199px;height:50px;background:var(--footer)}
.footer .name{position:absolute;left:190px;top:10px;font-size:13px;font-weight:700;color:var(--white)}
.footer .tag{position:absolute;left:190px;top:29px;font-size:9px;color:#ccc}
.footer .legal{position:absolute;right:190px;top:12px;font-size:9px;color:#ccc}
</style>
</head>
<body>
<div class="backdrop-top"></div>
<div class="backdrop-band"></div>
<div class="backdrop-fade"></div>

<header>
  <div class="utility-bar">
    <div class="follow">follow us on social network <span class="net"></span><span class="net"></span><span class="net"></span></div>
    <div class="support">Click here for live Support &nbsp;Tel: 1-800-555-0142</div>
    <div class="search">Search<span class="go"></span></div>
  </div>
  <div class="logo"><div class="name">BrightLoop</div><div class="tag">social media marketing company</div></div>
  <nav class="nav"><a class="current" href="#">Home</a><a href="#">Services</a><a href="#">Order</a><a href="#">Contact Us</a></nav>
  <div class="rule"></div>
</header>

<div class="hero" role="img" aria-label="Night photograph of illuminated city skyscrapers with light trails on a road"></div>

<section class="panel welcome">
  <h2>Welcome to BrightLoop.com</h2>
  <div class="icon" role="img" aria-label="Clipboard and pen icon"></div>
  <p>Lorem ipsum dolor sit amet, consectetur adipiscing elit. Pellentesque diam ligula egestas eget rhoncus vel, hendrerit in sem. Vivamus laoreet erat sit amet ante ullamcorper vestibulum. Duis porta, nisl quis cursus volutpat, est nulla placerat mauris, ut viverra leo ante sed leo. Vivamus fermentum dignissim sem, quis pellentesque dolor posuere vitae lorem ligula congue nibh.</p>
</section>

<section class="panel why">
  <h2>Why Choose Us</h2>
  <div class="icon" role="img" aria-label="Wooden chest with green download arrow icon"></div>
  <p>Ad mea brute deterruisset periculis duo, no exerci copiosae ius, ius nostrud offendit accommodare at. Ei vel facilis singulis semno, vis quaestio consetetur mod malorum deterruisset periculis duo, no aliis exerci copiosae ius, ius nostrud offendit accommodare at. Eam facilis singulis semno, vis quaestio consetetur.</p>
</section>

<div class="divider"></div>

<section class="step s1">
  <h3>Establish social media presence</h3>
  <span class="sub">Sed congue, dui vel tristique mollis...</span>
  <div class="banner" role="img" aria-label="Soft pink banner for social media presence">Social<b>Media</b>Presence</div>
  <p>Lorem ipsum dolor sit amet, consectetur adipiscing elit. Aenean commodo ligula eget dolor. Aenean massa. Cum sociis natoque penatibus et magnis dis parturient montes, nascetur ridiculus mus.</p>
  <a class="more" href="#">read more »</a>
</section>

<section class="step s2">
  <h3>Media management and advertising</h3>
  <span class="sub">Sed congue, dui vel tristique mollis...</span>
  <div class="banner" role="img" aria-label="Green banner for media management and advertising"><span style="font-size:14px">Media</span><b style="font-size:14px">Management</b><span style="font-size:14px">Advertising</span></div>
  <p>Aenean massa. Cum sociis natoque penatibus et magnis dis parturient montes, nascetur ridiculus mus. Donec quam felis, ultricies nec, pellentesque eu, pretium quis, sem. Nulla consequat massa quis enim.</p>
  <a class="more" href="#">read more »</a>
</section>

<section class="step s3">
  <h3>Analyze and engage</h3>
  <span class="sub">Sed congue, dui vel tristique mollis...</span>
  <div class="banner" role="img" aria-label="Blue banner for analyze and engage">Analyze<b>And</b>Engage</div>
  <p>Lorem ipsum dolor sit amet, consectetur adipiscing elit. Pellentesque diam ligula egestas eget rhoncus vel, hendrerit in sem. Vivamus laoreet erat sit amet ante ullamcorper vestibulum. Duis porta, nisl quis cursus volutpat, est nulla placerat mauris, ut viverra leo ante sed leo.</p>
  <a class="more" href="#">read more »</a>
</section>

<footer class="footer">
  <div class="name">BrightLoop</div>
  <div class="tag">social media marketing company</div>
  <div class="legal">© Copyright BrightLoop - All Rights Reserved | Home | Contact | RSS</div>
</footer>
</body>
</html>
```